Business Card Design Project - bel soravin group

dear Sirs

we need business card design for our group ( BEL Soravin Group ) , i have got the Logo design of our group from pixel harbor in previous , so all need details relating to our group i think available with you, as well as the the chosen logo design

we hope to provide us with business card logo that to be appropaite and satisfactory to us .

thanks

note : logo design of our group is attached .
Updates

Reason: please extend the deadline of my project for additional 15 days because i didn't received appropriate design for our gruop yet . kindly beaware that i have received 77 design till now , supossed to send me 200-250 design at least . thanks

Target Market(s)

contents
-

name : Korvan EL Mistrani

position : Operation Manager

Industry/Entity Type

Business

Requirements
Must have

• person name

group logo
Nice to have
• logo color matching with back background

```html
<!DOCTYPE html>
<html lang="en">
<head>
<meta charset="utf-8">
<title>BEL Soravin Group – Business Card</title>
<link href="https://fonts.googleapis.com/css2?family=Open+Sans:wght@400;600;700&display=swap" rel="stylesheet">
<style>
  :root{
    --page:#e9e7e3;
    --card-white:#ffffff;
    --card-dark:#2b2a2c;
    --band-dark:#2e2e30;
    --brand-blue:#1f6fb2;
    --brand-blue-deep:#1a5d97;
    --ink:#333333;
    --ink-soft:#4a4a4a;
    --band-text:#b9b9b9;
    --white:#ffffff;
  }
  *{box-sizing:border-box;margin:0;padding:0}
  html,body{width:1200px;height:900px;overflow:hidden}
  body{background:var(--page);font-family:"Open Sans",Arial,sans-serif;position:relative}

  .card{position:absolute;left:285px;width:630px;height:360px;border-radius:3px;
        box-shadow:0 6px 18px rgba(0,0,0,.18);overflow:hidden}
  .card--back{top:50px;background:var(--card-dark)}
  .card--front{top:470px;background:var(--card-white)}

  .brand{display:flex;align-items:center;gap:10px;color:var(--brand-blue);
         font-weight:700;letter-spacing:.5px;text-transform:uppercase}
  .brand__mark{width:14px;height:14px;background:var(--brand-blue)}

  .card--back .brand{position:absolute;left:0;right:0;top:140px;justify-content:center;font-size:34px}
  .card--back .brand__mark{width:22px;height:22px}
  .card--back .web{position:absolute;left:0;right:0;top:250px;text-align:center;
                   color:var(--white);font-size:14px}

  .card--front .brand{position:absolute;left:36px;top:36px;font-size:24px}

  .contacts{position:absolute;left:40px;top:160px;list-style:none}
  .contacts li{display:flex;align-items:center;gap:12px;height:22px;font-size:14px;color:var(--ink)}
  .contacts svg{width:14px;height:14px;fill:var(--brand-blue-deep)}

  .person{position:absolute;right:40px;top:178px;text-align:right}
  .person__name{font-size:22px;font-weight:700;color:var(--brand-blue-deep)}
  .person__role{font-size:13px;color:var(--ink-soft);margin-top:2px}

  .bands{position:absolute;left:0;bottom:0;width:630px;height:90px}
  .address{position:absolute;left:40px;bottom:58px;font-size:13px;color:var(--band-text)}
  .card--front .web{position:absolute;right:40px;bottom:16px;font-size:16px;font-weight:600;color:var(--white)}
</style>
</head>
<body>

<section class="card card--back" aria-label="Card back">
  <div class="brand"><span class="brand__mark"></span>BEL Soravin Group</div>
  <p class="web">www.belsoravin.com</p>
</section>

<section class="card card--front" aria-label="Card front">
  <div class="brand"><span class="brand__mark"></span>BEL Soravin Group</div>

  <ul class="contacts">
    <li><svg viewBox="0 0 16 16"><path d="M2 6c0-2 3-4 6-4s6 2 6 4v1h-3V5H5v2H2z M4 8h8l1 6H3z"/></svg>+1 415 260 3381</li>
    <li><svg viewBox="0 0 16 16"><path d="M4 1h8v4H4z M1 6h14v6h-3v3H4v-3H1z M5 10v4h6v-4z"/></svg>+1 415 260 3390</li>
    <li><svg viewBox="0 0 16 16"><path d="M4 1h8v14H4z M5 3v7h6V3z M7 12h2v1H7z" fill-rule="evenodd"/></svg>+1 628 447 9052</li>
    <li><svg viewBox="0 0 16 16"><path d="M1 3h14v10H1z M2 4l6 5 6-5z" fill-rule="evenodd"/></svg>korvan@belsoravin.com</li>
  </ul>

  <div class="person">
    <p class="person__name">Korvan EL Mistrani</p>
    <p class="person__role">Operation Manager</p>
  </div>

  <svg class="bands" viewBox="0 0 630 90" preserveAspectRatio="none" aria-hidden="true">
    <rect x="0" y="0" width="630" height="90" fill="var(--band-dark)"/>
    <polygon points="0,34 390,34 390,42 0,42" fill="var(--brand-blue)"/>
    <polygon points="380,42 408,14 630,14 630,90 0,90 0,42" fill="var(--brand-blue)"/>
  </svg>
  <p class="address">P.O.BOX 5821 Harborview, CN 4470</p>
  <p class="web">www.belsoravin.com</p>
</section>

</body>
</html>
```